Basic images needed for business powerpoint slides

We need basic images for a powerpoint design. The designs should be clean, modern, simple and easy to read on a screen and if they were printed on paper. The images should not be overly designed (no fancy graphics or ornate fonts), but should still look professional.

Please pay attention to the attachments that have sketches of the images that are needed. In the notes section of the powerpoint slides specifies additional details for each image.

Also, please adhere to the design guidelines that are also uploaded. Only use colors and fonts that are specified. The final images should be similar to the look and feel of the images in the design guidelines.
Updates

Designers -
Thanks for all your submissions! I am reviewing all the designs with my team and will have a decision ready by Sunday evening. If you are submitting any new designs, please submit by Sunday morning EST so my team can review them.

Thanks!

Target Market(s)

business executives

Industry/Entity Type

Business

Requirements
Must have
• Must Have:
- 1. Please see the attached powerpoint for the sketches we would like to have recreated. There are specific notes in each slide with additional details.

2. Please refer to the following pages in the uploaded design guideline document:
Colors - p. 14
- Use either the bright or muted color options as specified in the color scheme on this page

Typography - p. 16-17
- Use either helvetica or arial options

Powerpoint guidelines - p.42
- see for example of the general look and feel of the company

```html
<!DOCTYPE html>
<html lang="en">
<head>
<meta charset="UTF-8">
<title>Stakeholder Circles</title>
<link rel="stylesheet" href="https://fonts.googleapis.com/css2?family=Arimo:wght@400&display=swap">
<style>
  :root {
    --bg: #ffffff;
    --outer-ring: #fbf0cb;
    --teal-ring: #67b4b3;
    --tan-ring: #e2d2a8;
    --core: #cdc8a0;
    --divider: #eee0b8;
    --muted-text: #a99f87;
    --active-text: #111111;
  }
  html, body {
    margin: 0;
    padding: 0;
    width: 1198px;
    height: 1200px;
    overflow: hidden;
    background: var(--bg);
  }
  .diagram {
    display: block;
    width: 1198px;
    height: 1200px;
    font-family: "Arimo", Arial, Helvetica, sans-serif;
  }
  .ring-outer { fill: var(--outer-ring); }
  .ring-teal { fill: var(--teal-ring); }
  .ring-tan { fill: var(--tan-ring); }
  .core { fill: var(--core); }
  .divider { stroke: var(--divider); stroke-width: 1.5; }
  .label { fill: var(--muted-text); font-size: 14px; text-anchor: middle; }
  .number { fill: var(--muted-text); font-size: 28px; text-anchor: middle; }
  .label.is-active, .number.is-active { fill: var(--active-text); }
</style>
</head>
<body>
<svg class="diagram" viewBox="0 0 605 606" xmlns="http://www.w3.org/2000/svg" role="img" aria-label="Concentric stakeholder circles, level 14 Legal Analysts highlighted">
  <defs>
    <filter id="soft-shadow" x="-10%" y="-10%" width="125%" height="125%">
      <feDropShadow dx="4" dy="5" stdDeviation="4" flood-color="#5a4e30" flood-opacity="0.35"/>
    </filter>
  </defs>

  <circle class="ring-outer" cx="303" cy="303" r="302"/>
  <circle class="ring-teal" cx="303" cy="303" r="250" filter="url(#soft-shadow)"/>
  <circle class="ring-tan" cx="303" cy="303" r="200" filter="url(#soft-shadow)"/>

  <g class="dividers">
    <line class="divider" x1="303" y1="303" x2="303" y2="103"/>
    <line class="divider" x1="303" y1="303" x2="130" y2="403"/>
    <line class="divider" x1="303" y1="303" x2="476" y2="403"/>
  </g>

  <circle class="core" cx="303" cy="303" r="152" opacity="0.85"/>
  <g class="dividers">
    <line class="divider" x1="303" y1="303" x2="303" y2="151" opacity="0.6"/>
    <line class="divider" x1="303" y1="303" x2="171" y2="379" opacity="0.6"/>
    <line class="divider" x1="303" y1="303" x2="435" y2="379" opacity="0.6"/>
  </g>

  <g class="level level-15">
    <text class="label" x="300" y="22">Franchise Lawyers</text>
    <text class="label" x="300" y="35">Finance</text>
    <text class="label" x="302" y="48">Committee Members</text>
    <text class="number" x="410" y="50">15</text>
  </g>

  <g class="level level-14">
    <text class="label is-active" x="292" y="85">Legal Analysts</text>
    <text class="number is-active" x="369" y="91">14</text>
  </g>

  <g class="level level-13">
    <text class="number" x="305" y="131">13</text>
    <text class="label" x="305" y="150">Physicians,Clinicians, Scientists</text>
  </g>

  <g class="level level-10">
    <text class="number" x="238" y="229">10</text>
    <text class="label" x="232" y="257">HFAC Specialists</text>
    <text class="label" x="232" y="275">(Med Products-</text>
    <text class="label" x="232" y="291">Med Affairs)</text>
  </g>

  <g class="level level-11">
    <text class="number" x="363" y="229">11</text>
    <text class="label" x="373" y="257">HFAC Specialists</text>
    <text class="label" x="373" y="275">(Bio Science-</text>
    <text class="label" x="373" y="291">Med Affairs)</text>
  </g>

  <g class="level level-12">
    <text class="number" x="305" y="372">12</text>
    <text class="label" x="305" y="392">HFAC Specialists</text>
    <text class="label" x="305" y="410">(Contributions Management</text>
    <text class="label" x="305" y="426">Program)</text>
  </g>

  <g class="level level-external">
    <text class="label" x="306" y="480">External Orgs</text>
  </g>
</svg>
</body>
</html>
```